Webseite für Klempnerei Wendlin GmbH
Zielgruppe
Traditionsreicher Familienbetrieb: Klempnerei für Heizung, Bäder nach Maß und Sanitär, Dachklempnerei, Solar, alternative Energien
Aufgabenstellung
Die Farben der Webseite sollen bitte die gleichen, wie auf der alten Seite sein.
Also blau mit Akzenten in vorwiegend rot und ein wenig gelb.
Insgesamt soll die Webseite klar strukturiert sein, aber dennoch modern wirken.
Die Navigationsleiste bitte in folgender Reihenfolge:
-Start
- Das sind wir
-Leistungsübersicht
- Referenzen
- aktuelle Meldungen
- Kontakt
Die Startseite soll wie folgt gestaltet sein und Call to action wahllos in der Startseite evrteilen:
- großes Headerbild
-Teaser zu' Das sind wir' - Familientradition betonen
- Leistungsübersicht in Boxen mit großem Bild und angedeuteter Verlinkung zu der Leistungsunterseite: Heizung, Bäder nach Maß, Dachklempnerei, Solar, alternative Energien
-Teaser zu Referenzen
- Teaser zu aktuelle Meldungen
- Kontakt mit Map
- Footer mit Aufführung: Mitglied der Innung
-Datenschutz und Impressum
Bei den Inhalten bitte an der alten Webseite orientieren: https://www.heizung-wendlin.example/#
Bilder bitte entsprechende Vorschlagen

```html
<!DOCTYPE html>
<html lang="de">
<head>
<meta charset="utf-8">
<title>Klempnerei Wendlin GmbH – Kontakt</title>
<link rel="stylesheet" href="https://fonts.googleapis.com/css2?family=Montserrat:wght@300;400;600;700&family=Roboto+Condensed:wght@400&display=swap">
<style>
  :root {
    --canvas: #f2f2f2;
    --page: #ffffff;
    --ink: #1d1d1d;
    --brand-blue: #3f51a3;
    --contact-deep: #0c4877;
    --contact-mid: #24506d;
    --contact-soft: #627d7c;
    --band: rgba(150, 175, 190, 0.45);
    --field: rgba(236, 237, 239, 0.95);
    --field-text: #2a2a2a;
    --footer-start: #45599e;
    --footer-end: #163d49;
    --light: #ffffff;
    --rule: #555555;
    --badge-outer: #1a86d6;
  }
  * { box-sizing: border-box; margin: 0; padding: 0; }
  html, body { width: 1200px; height: 1200px; overflow: hidden; }
  body {
    background: var(--canvas);
    font-family: "Montserrat", Arial, sans-serif;
    color: var(--ink);
    position: relative;
  }
  .page {
    position: absolute; left: 158px; top: 0; width: 884px; height: 1151px;
    background: var(--page);
    box-shadow: 0 6px 14px rgba(0,0,0,0.25);
    overflow: hidden;
  }
  .news-teaser { position: absolute; left: 0; top: 0; width: 884px; height: 283px; }
  .news-photo-left {
    position: absolute; left: 0; top: 0; width: 231px; height: 176px;
    background: linear-gradient(100deg, #6f6a5f 0%, #8c8a80 30%, #aac2dc 45%, #c9d8ea 70%, #8fb0d6 100%);
  }
  .news-photo-right {
    position: absolute; left: 642px; top: 0; width: 242px; height: 254px;
    background: linear-gradient(160deg, #b9bcc2 0%, #7d848f 35%, #2c4f8c 65%, #1a3f86 100%);
  }
  .news-text {
    position: absolute; left: 300px; top: -4px; width: 284px; text-align: center;
    font-size: 10px; line-height: 14px; letter-spacing: 0.9px; font-weight: 400;
  }
  .news-button {
    position: absolute; left: 362px; top: 60px; width: 151px; height: 36px;
    background: var(--brand-blue); color: var(--light);
    font-size: 10px; font-weight: 700; letter-spacing: 2.6px;
    display: flex; align-items: center; justify-content: center;
  }
  .news-rule { position: absolute; left: 0; top: 229px; width: 401px; height: 1px; background: var(--rule); }

  .contact {
    position: absolute; left: 0; top: 283px; width: 884px; height: 507px;
    background: linear-gradient(100deg, var(--contact-deep) 0%, var(--contact-mid) 45%, var(--contact-soft) 100%);
  }
  .contact-headline { position: absolute; left: 0; top: 102px; }
  .headline-band {
    position: absolute; left: 0; height: 35px; background: var(--band);
    color: var(--light); font-size: 27px; font-weight: 400; letter-spacing: 4.4px;
    line-height: 35px; padding-left: 48px; white-space: nowrap;
  }
  .headline-band.first { top: 0; width: 286px; }
  .headline-band.second { top: 39px; width: 318px; }
  .contact-copy {
    position: absolute; left: 50px; top: 205px; width: 240px;
    color: var(--light); font-size: 10px; line-height: 14.3px; letter-spacing: 0.8px;
  }
  .field {
    position: absolute; background: var(--field); color: var(--field-text);
    font-family: "Roboto Condensed", Arial, sans-serif; font-size: 13px;
    padding-left: 12px; display: flex; align-items: center;
  }
  .field-name { left: 349px; top: 167px; width: 144px; height: 32px; }
  .field-surname { left: 502px; top: 167px; width: 144px; height: 32px; }
  .field-email { left: 349px; top: 210px; width: 293px; height: 32px; padding-left: 14px; }
  .field-phone { left: 651px; top: 210px; width: 125px; height: 32px; padding-left: 14px; }
  .field-message { left: 349px; top: 252px; width: 427px; height: 102px; align-items: flex-start; padding: 14px 18px; }
  .contact-button {
    position: absolute; left: 349px; top: 372px; width: 146px; height: 35px;
    border: 1px solid var(--light); color: var(--light);
    font-size: 9.5px; font-weight: 700; letter-spacing: 2.6px;
    display: flex; align-items: center; justify-content: center;
  }

  .map {
    position: absolute; left: 0; top: 790px; width: 884px; height: 180px;
    background: linear-gradient(90deg, #eceef1 0%, #e5eaf0 30%, #dfe9ee 45%, #eceef1 60%, #e3efe6 100%);
  }

  .footer {
    position: absolute; left: 0; top: 970px; width: 884px; height: 181px;
    background: linear-gradient(90deg, var(--footer-start) 0%, var(--footer-end) 80%);
    color: var(--light); font-size: 10px; letter-spacing: 1px;
  }
  .footer-address { position: absolute; left: 50px; top: 44px; line-height: 14.5px; }
  .footer-address .company { margin-bottom: 14px; }
  .footer-reach { position: absolute; left: 272px; top: 55px; line-height: 14.5px; }
  .footer-reach .row { display: flex; }
  .footer-reach .label { width: 45px; }
  .footer-reach .gap { height: 14.5px; }
  .footer-links { position: absolute; top: 143px; left: 0; font-size: 9.5px; letter-spacing: 3px; }
  .footer-links span { position: absolute; white-space: nowrap; }
  .guild-badge { position: absolute; left: 694px; top: 38px; }
</style>
</head>
<body>
  <main class="page">
    <section class="news-teaser">
      <div class="news-photo-left" role="img" aria-label="Foto: Hausfassade von unten gegen blauen Himmel mit Wolken"></div>
      <p class="news-text">consectetur adipiscing elit. Fusce quis quam non enim blandit te</p>
      <div class="news-button">Zu den News.</div>
      <div class="news-rule"></div>
      <div class="news-photo-right" role="img" aria-label="Foto: Handwerker montiert ein Solarmodul"></div>
    </section>

    <section class="contact" role="img" aria-label="Hintergrundfoto: Hände mit Smartphone, blau getönt">
      <div class="contact-headline">
        <div class="headline-band first">Wir freuen uns</div>
        <div class="headline-band second">auf Ihre Anfrage.</div>
      </div>
      <p class="contact-copy">Lorem ipsum dolor sit amet, consectetur adipiscing elit. Fusce quis quam non enim blandit tempor. Proin ac tellus accumsan leo sagitti.Lorem ipsum dolor sit amet, consectetur adipiscing elit. Fusce quis quam non enim blandit te</p>
      <div class="field field-name">Name</div>
      <div class="field field-surname">Nachname</div>
      <div class="field field-email">E-Mail Adresse</div>
      <div class="field field-phone">Telefon</div>
      <div class="field field-message">Nachricht</div>
      <div class="contact-button">Kontaktieren.</div>
    </section>

    <section class="map" role="img" aria-label="Stadtplan mit Standort des Betriebs"></section>

    <footer class="footer">
      <div class="footer-address">
        <div class="company">Wendlin GmbH</div>
        <div>OT Lindenau-Bergheim</div>
        <div>Mühlenweg 42</div>
        <div>09999 Musterstadt</div>
      </div>
      <div class="footer-reach">
        <div class="row"><span class="label">Tel.:</span><span>01234 567890</span></div>
        <div class="row"><span class="label">Fax:</span><span>01234 567891</span></div>
        <div class="gap"></div>
        <div class="row"><span class="label">E-Mail:</span><span>info@heizung-wendlin.example</span></div>
      </div>
      <nav class="footer-links">
        <span style="left:53px">Datenschutz</span>
        <span style="left:190px">Impressum</span>
        <span style="left:326px">Kontakt</span>
      </nav>
      <svg class="guild-badge" width="108" height="108" viewBox="0 0 108 108" role="img" aria-label="Mitglied der Innung">
        <circle cx="54" cy="54" r="53" fill="var(--badge-outer)"/>
      </svg>
    </footer>
  </main>
</body>
</html>
```